Flyer-Design für Energy-Drink
Zielgruppe
Es geht um einen neuen, gesunden Energy-Drink
Aufgabenstellung
Der Flyer sollte A5 entweder vorne und hinten bedruckt und ungefaltet sein
oder
A5 gefaltet auf A6 sein
Er soll junge Menschen ansprechen und hipp sein
Er soll erwachsene Menschen jeden Alters mit einem Gesundheitsbewusstsein ansprechen
Wichtig ist: kein Zuckerzusatz - 50% Fruchtanteil - ohne Chemie - absolut natürlich
wertvolle Vital und Inhaltsstoffe
einzigartiger, fruchtiger Geschmack, wenig Kohlensäure
gekühlt und geschüttelt trinken
Kick vor dem Sport oder einfach zwischendurch.
Neuer Antrieb
anregend, belebend
Dose ist zu 100% recycelbar

```html
<!DOCTYPE html>
<html lang="de">
<head>
<meta charset="utf-8">
<title>FRUXA – Flyer Vorder- und Rückseite</title>
<link rel="stylesheet" href="https://fonts.googleapis.com/css2?family=Bebas+Neue&family=Caveat+Brush&family=Raleway:wght@400;700;800&display=swap">
<style>
  :root {
    --stage: #e9e9e9;
    --ink: #0b0b0b;
    --ink-soft: #1c1c1c;
    --white: #f4f4f4;
    --gold: #f0a81c;
    --ember: #c8501a;
    --green: #1f8a3b;
    --muted: #b9b9b9;
  }
  * { box-sizing: border-box; margin: 0; padding: 0; }
  html, body { width: 1020px; height: 1200px; overflow: hidden; }
  body { background: var(--stage); position: relative; font-family: "Raleway", sans-serif; }

  .flyer {
    position: absolute; top: 268px; width: 470px; height: 664px;
    background: var(--ink); overflow: hidden; color: var(--white);
    box-shadow: 0 18px 40px rgba(0,0,0,.18);
  }
  .flyer--back { left: 25px; }
  .flyer--front { left: 525px; }

  .photo { position: absolute; left: 0; top: 0; width: 100%; }
  .flyer--back .photo {
    height: 330px;
    background: radial-gradient(ellipse at 60% 40%, #4a4a4a 0%, #262626 55%, var(--ink) 100%);
  }
  .flyer--front .photo {
    height: 400px;
    background: radial-gradient(ellipse at 50% 20%, #3d3d3d 0%, #1f1f1f 55%, var(--ink) 100%);
  }

  .glow {
    position: absolute; border-radius: 50%;
    background: radial-gradient(circle, rgba(200,80,26,.75) 0%, rgba(200,80,26,.25) 45%, transparent 70%);
  }

  .can {
    position: absolute; border-radius: 14px 14px 18px 18px;
    background: linear-gradient(90deg, #151515 0%, #6a0f0f 35%, #b3261a 50%, #5a0c0c 68%, #111 100%);
    border-top: 5px solid #c0201a;
  }
  .can-name {
    position: absolute; left: 50%; top: 50%;
    transform: translate(-50%, -50%) rotate(-90deg);
    font-family: "Raleway", sans-serif; font-weight: 800; color: var(--white);
    font-size: 40px; letter-spacing: 2px; white-space: nowrap;
  }

  /* back side */
  .kicker {
    position: absolute; left: 40px; top: 62px; width: 400px;
    font-family: "Bebas Neue", sans-serif; font-size: 44px; line-height: 1.05;
    color: var(--gold); letter-spacing: .5px;
  }
  .kicker .plain { color: var(--white); }
  .benefits {
    position: absolute; left: 225px; top: 200px; list-style: none;
    font-family: "Bebas Neue", sans-serif; font-size: 29px; line-height: 36px;
  }
  .benefits .hl { color: var(--gold); }
  .flyer--back .can { left: 62px; top: 205px; width: 130px; height: 290px; }
  .flyer--back .can-name { font-size: 44px; }

  .contact { position: absolute; left: 40px; top: 530px; font-size: 12px; line-height: 20px; }
  .wordmark { font-weight: 800; color: var(--gold); letter-spacing: 1px; }
  .contact .wordmark { font-size: 20px; margin-bottom: 4px; }
  .contact dt { font-weight: 700; float: left; width: 50px; clear: left; }
  .contact dd { color: var(--muted); }
  .contact .lead { font-weight: 700; }
  .social { display: flex; gap: 8px; align-items: center; margin-top: 10px; font-weight: 700; }
  .social span.dot { width: 24px; height: 24px; border-radius: 50%; background: var(--white); display: inline-block; }

  .recycle {
    position: absolute; right: 40px; top: 520px; width: 130px; height: 118px;
    border: 2px solid var(--green); border-radius: 10px;
    display: flex; flex-direction: column; align-items: center; justify-content: center; gap: 8px;
    font-size: 12px; font-weight: 700; text-align: center; line-height: 1.25;
  }

  /* front side */
  .slogan {
    position: absolute; left: 0; top: 70px; width: 100%; text-align: center;
    font-family: "Caveat Brush", cursive; font-size: 62px; line-height: .95; color: var(--white);
  }
  .bubble {
    position: absolute; font-family: "Bebas Neue", sans-serif; font-size: 28px; line-height: 1;
    text-align: center; color: var(--white);
  }
  .bubble svg { position: absolute; left: 0; top: 0; overflow: visible; }
  .bubble span { position: relative; display: block; padding: 12px 14px; }
  .bubble--drive { left: 48px; top: 300px; width: 118px; }
  .bubble--lively { left: 300px; top: 395px; width: 128px; }
  .flyer--front .can { left: 180px; top: 305px; width: 110px; height: 230px; }
  .flyer--front .can-name { font-size: 36px; }

  .pitch { position: absolute; left: 36px; top: 548px; width: 250px; font-size: 11.5px; line-height: 1.55; color: var(--muted); }
  .pitch strong { color: var(--gold); font-weight: 700; }
  .pitch .wordmark { font-size: 15px; }
  .front-mark { position: absolute; right: 36px; top: 590px; display: flex; align-items: center; gap: 10px; }
  .front-mark .ring { width: 30px; height: 30px; border-radius: 50%; background: var(--ember); }
  .front-mark .wordmark { font-size: 34px; }
</style>
</head>
<body>

<section class="flyer flyer--back" aria-label="Flyer Rückseite">
  <div class="photo" role="img" aria-label="Dunkles Sportstadion im Nebel"></div>
  <h2 class="kicker">Kick vor dem Sport <span class="plain">oder</span><br>einfach zwischendurch.</h2>
  <div class="glow" style="left:0;top:240px;width:260px;height:260px"></div>
  <div class="can" role="img" aria-label="Getränkedose FRUXA">
    <span class="can-name">FRUXA</span>
  </div>
  <ul class="benefits">
    <li>- Kein Zuckerzusatz</li>
    <li>- <span class="hl">50%</span> Fruchtanteil</li>
    <li>- Ohne Chemie</li>
    <li>- Absolut natürlich</li>
    <li>- Inhaltsstoffe</li>
    <li>- Fruchtiger Geschmack</li>
    <li>- Wenig Kohlensäure</li>
  </ul>
  <div class="contact">
    <div class="wordmark">FRUXA</div>
    <p class="lead">Customer Support</p>
    <dl>
      <dt>Tel :</dt><dd>0123 - 4567 - 8</dd>
      <dt>Email :</dt><dd>support@fruxadrink.de</dd>
      <dt>Web :</dt><dd>www.fruxadrink.de</dd>
    </dl>
    <div class="social"><span class="dot"></span><span class="dot"></span><span class="dot"></span><span>@fruxadrink</span></div>
  </div>
  <div class="recycle">
    <svg width="44" height="40" viewBox="0 0 44 40" aria-hidden="true"><polygon points="22,2 42,38 2,38" fill="none" stroke="var(--green)" stroke-width="5"/></svg>
    <span>Dose ist zu<br>100% recycelbar</span>
  </div>
</section>

<section class="flyer flyer--front" aria-label="Flyer Vorderseite">
  <div class="photo" role="img" aria-label="Footballspieler mit Helm im Dunkeln"></div>
  <h1 class="slogan">gekühlt und<br>geschüttelt<br>trinken</h1>
  <div class="glow" style="left:110px;top:360px;width:250px;height:220px"></div>
  <div class="can" role="img" aria-label="Getränkedose FRUXA">
    <span class="can-name">FRUXA</span>
  </div>
  <div class="bubble bubble--drive">
    <svg width="118" height="82" viewBox="0 0 118 82" aria-hidden="true"><path d="M4 4 H114 V64 H62 L52 78 L48 64 H4 Z" fill="var(--ink)" stroke="var(--white)" stroke-width="2.5" stroke-linejoin="round"/></svg>
    <span>Neuer<br>Antrieb</span>
  </div>
  <div class="bubble bubble--lively">
    <svg width="128" height="86" viewBox="0 0 128 86" aria-hidden="true"><path d="M4 4 H124 V66 H30 L10 80 L16 66 H4 Z" fill="var(--ink)" stroke="var(--white)" stroke-width="2.5" stroke-linejoin="round"/></svg>
    <span>Anregend<br>belebend</span>
  </div>
  <p class="pitch"><span class="wordmark">FRUXA</span> ist der neue <strong>Healthy Energy Drink</strong>. Sie können ihn vor dem Sport oder zwischendurch trinken. Er hat <strong>50% Fruchtanteil</strong> | <strong>Natürlich | Wenig Kohlensäure | Ohne Chemie |</strong></p>
  <div class="front-mark"><span class="ring"></span><span class="wordmark">FRUXA</span></div>
</section>

</body>
</html>
```